Covid19 Poster for workplaces

Create a poster on how to protect yourself from Corona virus at work.
We are a Staffwell Care company. We have just re-branded so we need to fit in with our brand. We like clean and fresh, slightly amusing is ok if it will draw attention but it's an important topic. A4 and A3 please.

Content:

Headline: Lower the risk of COVID 19 in the workplace.

BE WELL

Bring your own cup - don’t share cups and food.
Elbow tap instead of handshakes and kisses
Wash your hands often - with soap.
Elbow or tissues when you cough or sneeze then straight in the bin
Leave your face alone after touching shared surfaces
Leave your bugs at home if you’re feeling unwell.

Call health line if you have a cough, a high temperature and shortness of breath. 0800 472 9160

Based on recommendations from ZPK and QLN

Target Market(s)

Employees - so anyone

Other font styles liked:
• Use the closest font to the brand documents

Requirements
Should not have
• Clip art

```html
<!DOCTYPE html>
<html lang="en">
<head>
<meta charset="utf-8">
<title>Lower the risk of COVID 19 in the workplace</title>
<link rel="stylesheet" href="https://fonts.googleapis.com/css2?family=Montserrat:wght@500;600;700;800;900&display=swap">
<style>
  :root {
    --ink-black: #111314;
    --lime: #8cc63f;
    --cyan: #2bb8e6;
    --sky: #2a9fd6;
    --navy: #1c3a78;
    --mist: #eaf6f8;
    --mist-deep: #d7eef2;
    --watermark: #cfeaf0;
    --teal: #25b4c6;
    --white: #ffffff;
    --virus: #e38a3a;
    --office: #f2b34a;
  }
  * { box-sizing: border-box; margin: 0; padding: 0; }
  html, body { width: 849px; height: 1200px; overflow: hidden; background: var(--white); }
  body { font-family: "Montserrat", Arial, sans-serif; }

  .poster { position: relative; width: 849px; height: 1200px; overflow: hidden; background: var(--mist); }

  .header-shape { position: absolute; left: 0; top: 0; width: 849px; height: 420px; }

  .headline { position: absolute; left: 40px; top: 28px; color: var(--white); }
  .headline__lead { font-size: 38px; font-weight: 700; line-height: 1.1; }
  .headline__main { font-size: 84px; font-weight: 900; color: var(--cyan); line-height: 1; letter-spacing: 1px; }
  .headline__tail { font-size: 42px; font-weight: 800; line-height: 1.1; }
  .headline__source { margin-top: 10px; font-size: 16px; font-weight: 600; line-height: 1.3; }

  .office-scene { position: absolute; left: 470px; top: 40px; width: 350px; height: 270px;
    border-radius: 24px; background: linear-gradient(160deg, var(--office), #dfe8ea 70%); }

  .virus { position: absolute; border-radius: 50%; background: radial-gradient(circle, var(--virus) 55%, #c86a22); }

  .watermark { position: absolute; left: -40px; top: 1080px; transform-origin: left top; transform: rotate(-90deg);
    font-size: 150px; font-weight: 900; color: var(--watermark); white-space: nowrap; letter-spacing: 4px; line-height: 1; }
  .watermark--second { left: 120px; font-size: 110px; top: 860px; }

  .tips-title { position: absolute; left: 345px; top: 408px; font-size: 62px; font-weight: 900; color: var(--sky); letter-spacing: 2px; }

  .tips { position: absolute; left: 235px; top: 485px; width: 590px; list-style: none; }
  .tip { display: flex; align-items: center; height: 96px; margin-bottom: 0; }
  .tip__icon { flex: 0 0 84px; height: 84px; border-radius: 50%; background: var(--mist-deep);
    border: 4px solid var(--white); box-shadow: 0 0 0 2px var(--mist-deep); }
  .tip__text { margin-left: 26px; font-size: 23px; font-weight: 700; color: var(--navy); line-height: 1.22; white-space: nowrap; }

  .footer { position: absolute; left: 0; bottom: 0; width: 849px; height: 124px; background: var(--teal);
    color: var(--white); display: flex; align-items: center; justify-content: space-between; padding: 0 40px; }
  .footer__info { font-size: 18px; font-weight: 700; line-height: 1.3; }
  .footer__phone { font-size: 36px; font-weight: 800; letter-spacing: 1px; margin-top: 4px; }
  .brand { display: flex; align-items: center; gap: 14px; font-size: 30px; font-weight: 800; line-height: 1.05; }
  .brand__dot { width: 40px; height: 40px; border-radius: 50%; background: var(--white); }
</style>
</head>
<body>
<main class="poster">
  <svg class="header-shape" viewBox="0 0 849 420" aria-hidden="true">
    <path d="M0 0 H849 V150 C760 250 640 300 520 320 C360 345 220 390 0 420 Z" fill="var(--lime)"/>
    <path d="M0 0 H849 V90 C760 170 640 220 520 245 C360 275 200 300 0 340 Z" fill="var(--ink-black)"/>
  </svg>

  <div class="office-scene" role="img" aria-label="Illustration of colleagues working together around a desk in an office"></div>

  <div class="virus" role="img" aria-label="Virus particle illustration" style="left:20px;top:250px;width:60px;height:60px"></div>
  <div class="virus" role="img" aria-label="Virus particle illustration" style="left:360px;top:220px;width:70px;height:70px"></div>
  <div class="virus" role="img" aria-label="Virus particle illustration" style="left:440px;top:30px;width:44px;height:44px"></div>
  <div class="virus" role="img" aria-label="Virus particle illustration" style="left:250px;top:300px;width:34px;height:34px"></div>

  <header class="headline">
    <p class="headline__lead">Lower the risk of</p>
    <h1 class="headline__main">COVID 19</h1>
    <p class="headline__tail">in the workplace</p>
    <p class="headline__source">Based on recommendations<br>from ZPK and QLN</p>
  </header>

  <div class="watermark" aria-hidden="true">BE WELL</div>
  <div class="watermark watermark--second" aria-hidden="true">BE WELL</div>

  <h2 class="tips-title">BE WELL</h2>

  <ul class="tips">
    <li class="tip"><span class="tip__icon" role="img" aria-label="Icon of a personal cup and food"></span><p class="tip__text">Bring your own cup<br>don’t share cups and food.</p></li>
    <li class="tip"><span class="tip__icon" role="img" aria-label="Icon of an elbow tap greeting"></span><p class="tip__text">Elbow tap instead of<br>handshakes and kisses</p></li>
    <li class="tip"><span class="tip__icon" role="img" aria-label="Icon of hands being washed with soap"></span><p class="tip__text">Wash your hands often<br>with soap.</p></li>
    <li class="tip"><span class="tip__icon" role="img" aria-label="Icon of coughing into an elbow"></span><p class="tip__text">Elbow or tissues when you cough<br>or sneeze then straight in the bin</p></li>
    <li class="tip"><span class="tip__icon" role="img" aria-label="Icon reminding not to touch your face"></span><p class="tip__text">Leave your face alone<br>after touching shared surfaces</p></li>
    <li class="tip"><span class="tip__icon" role="img" aria-label="Icon of staying home when unwell"></span><p class="tip__text">Leave your bugs at home<br>if you’re feeling unwell.</p></li>
  </ul>

  <footer class="footer">
    <div class="footer__info">
      <p>Call health line if you have a cough,<br>a high temperature and shortness of breath.</p>
      <p class="footer__phone">0800 472 9160</p>
    </div>
    <div class="brand">
      <span class="brand__dot" aria-hidden="true"></span>
      <span>Staffwell<br>Care</span>
    </div>
  </footer>
</main>
</body>
</html>
```